Infographic for a Life Transformation brand to showcase their principle method

I need a clean infographic which would be used in a brochure to show the 5 steps to achieving a Inner Uprising. (ie Life transformation). I use the theme of a revolution so I would like the graphic to include a raised fist or something to represent a revolution and then the 5 points of information to represent each step.
Needs to very clean and simple. I don't want something that would take up a full page, I want it as a graphic, almost like a big logo. I don't want it laid out like a process chart.

My brand personalities from https://markcharacterhub.com.au/ are
The Everyman and The Magician to give you an idea of my brand.

I've attached my logo so that you can see the colour of it. Graphic doesn't need to match logo but should align with that colour.

Target Market(s)

Top Tier Executives, males, 35-55y old

Industry/Entity Type

Life Coaching

Requirements
Must have
• The graphic must have the 5 Steps: in this order
1.Clarity
2. Measurement
3. Discipline
4. Nutrition
5.Exercise
Nice to have
• It could include these action steps which line up with the 5 steps, It may be too much information by there is the option to include if it works.
1.see it
2. track it
3. do it
4. eat it
5. move it

```html
<!DOCTYPE html>
<html lang="en">
<head>
<meta charset="utf-8">
<title>Inner Uprising – Five Steps</title>
<link rel="stylesheet" href="https://fonts.googleapis.com/css2?family=Varela+Round&display=swap">
<style>
  :root {
    --bg: #ececec;
    --navy: #0e4a8c;
    --ring-dark: #1d5596;
    --ring-light: #cfe4fb;
    --track: #cbdad8;
    --dash: #c9ccd8;
    --white: #ffffff;
    --fist-tone: #2c64a6;
  }
  html, body {
    margin: 0;
    padding: 0;
    width: 1200px;
    height: 900px;
    overflow: hidden;
    background: var(--bg);
  }
  .canvas {
    position: relative;
    width: 1200px;
    height: 900px;
    font-family: "Varela Round", "Nunito", sans-serif;
  }
  .canvas svg.stage {
    position: absolute;
    inset: 0;
  }
  .step-title {
    font-size: 27px;
    fill: var(--white);
    letter-spacing: 0.2px;
  }
  .step-action {
    font-size: 22px;
    fill: var(--white);
  }
  .step-number {
    font-size: 52px;
    fill: var(--white);
  }
  .emblem-fist {
    position: absolute;
    left: 328px;
    top: 305px;
    width: 208px;
    height: 288px;
    border-radius: 44% 44% 18% 18%;
    background: radial-gradient(circle at 50% 40%, #3a73b6, var(--fist-tone) 70%);
  }
</style>
</head>
<body>
<main class="canvas">
  <svg class="stage" width="1200" height="900" viewBox="0 0 1200 900" xmlns="http://www.w3.org/2000/svg">
    <defs>
      <filter id="soft-shadow" x="-20%" y="-20%" width="140%" height="150%">
        <feDropShadow dx="0" dy="5" stdDeviation="5" flood-color="#000" flood-opacity="0.22"/>
      </filter>
      <linearGradient id="ring-grad" x1="0" y1="0" x2="1" y2="0">
        <stop offset="0" stop-color="var(--ring-dark)"/>
        <stop offset="1" stop-color="var(--ring-light)"/>
      </linearGradient>

      <linearGradient id="band-green" x1="0" x2="1"><stop offset="0" stop-color="#34a548"/><stop offset="1" stop-color="#45d07a"/></linearGradient>
      <linearGradient id="gem-green" x1="0" y1="1" x2="1" y2="0"><stop offset="0" stop-color="#0d932c"/><stop offset="1" stop-color="#22c552"/></linearGradient>

      <linearGradient id="band-red" x1="0" x2="1"><stop offset="0" stop-color="#ff2d72"/><stop offset="1" stop-color="#ff3a3a"/></linearGradient>
      <linearGradient id="gem-red" x1="0" y1="1" x2="1" y2="0"><stop offset="0" stop-color="#e0003a"/><stop offset="1" stop-color="#ff1a40"/></linearGradient>

      <linearGradient id="band-teal" x1="0" x2="1"><stop offset="0" stop-color="#3aa68f"/><stop offset="1" stop-color="#33e6c8"/></linearGradient>
      <linearGradient id="gem-teal" x1="0" y1="1" x2="1" y2="0"><stop offset="0" stop-color="#16876f"/><stop offset="1" stop-color="#10d4a9"/></linearGradient>

      <linearGradient id="band-orange" x1="0" x2="1"><stop offset="0" stop-color="#f45a2c"/><stop offset="1" stop-color="#f7ad4b"/></linearGradient>
      <linearGradient id="gem-orange" x1="0" y1="1" x2="1" y2="0"><stop offset="0" stop-color="#ff3d00"/><stop offset="1" stop-color="#ffa61f"/></linearGradient>

      <linearGradient id="band-blue" x1="0" x2="1"><stop offset="0" stop-color="#6d5bf0"/><stop offset="1" stop-color="#3ec3f8"/></linearGradient>
      <linearGradient id="gem-blue" x1="0" y1="1" x2="1" y2="0"><stop offset="0" stop-color="#5c49f0"/><stop offset="1" stop-color="#17aaff"/></linearGradient>
    </defs>

    <!-- guide arcs -->
    <path class="guide-dashed" d="M499 177 A280 280 0 0 1 499 737" fill="none" stroke="var(--dash)" stroke-width="4" stroke-dasharray="12 7"/>
    <path class="guide-track" d="M499 210 A250 250 0 0 1 499 712" fill="none" stroke="var(--track)" stroke-width="20"/>

    <!-- emblem -->
    <g class="emblem" filter="url(#soft-shadow)">
      <circle cx="425" cy="451" r="203" fill="url(#ring-grad)"/>
      <circle cx="425" cy="451" r="187" fill="var(--navy)"/>
    </g>

    <!-- step markers -->
    <g class="step-markers" stroke="var(--white)" stroke-width="4" filter="url(#soft-shadow)">
      <circle cx="551" cy="233" r="15" fill="url(#gem-green)"/>
      <circle cx="643" cy="328" r="15" fill="url(#gem-red)"/>
      <circle cx="675" cy="451" r="15" fill="url(#gem-teal)"/>
      <circle cx="643" cy="589" r="15" fill="url(#gem-orange)"/>
      <circle cx="551" cy="685" r="15" fill="url(#gem-blue)"/>
    </g>

    <!-- step 1 -->
    <g class="step step-clarity" filter="url(#soft-shadow)">
      <path d="M661 134 H870 L919 176 L870 219 H661 Z" fill="url(#band-green)"/>
      <rect x="625" y="141" width="72" height="72" rx="6" transform="rotate(45 661 177)" fill="url(#gem-green)"/>
      <text class="step-number" x="661" y="196" text-anchor="middle">1</text>
      <text class="step-title" x="715" y="175">CLARITY</text>
      <text class="step-action" x="738" y="202">See It</text>
    </g>

    <!-- step 2 -->
    <g class="step step-measurement" filter="url(#soft-shadow)">
      <path d="M750 267 H959 L1008 309 L959 351 H750 Z" fill="url(#band-red)"/>
      <rect x="714" y="273" width="72" height="72" rx="6" transform="rotate(45 750 309)" fill="url(#gem-red)"/>
      <text class="step-number" x="750" y="328" text-anchor="middle">2</text>
      <text class="step-title" x="805" y="308">MEASUREMENT</text>
      <text class="step-action" x="828" y="335">Track It</text>
    </g>

    <!-- step 3 -->
    <g class="step step-discipline" filter="url(#soft-shadow)">
      <path d="M793 408 H1002 L1051 450 L1002 493 H793 Z" fill="url(#band-teal)"/>
      <rect x="757" y="414" width="72" height="72" rx="6" transform="rotate(45 793 450)" fill="url(#gem-teal)"/>
      <text class="step-number" x="793" y="469" text-anchor="middle">3</text>
      <text class="step-title" x="850" y="449">DISCIPLINE</text>
      <text class="step-action" x="873" y="476">Do It</text>
    </g>

    <!-- step 4 -->
    <g class="step step-nutrition" filter="url(#soft-shadow)">
      <path d="M750 549 H959 L1008 591 L959 633 H750 Z" fill="url(#band-orange)"/>
      <rect x="714" y="555" width="72" height="72" rx="6" transform="rotate(45 750 591)" fill="url(#gem-orange)"/>
      <text class="step-number" x="750" y="610" text-anchor="middle">4</text>
      <text class="step-title" x="805" y="590">NUTRITION</text>
      <text class="step-action" x="828" y="617">Eat It</text>
    </g>

    <!-- step 5 -->
    <g class="step step-exercise" filter="url(#soft-shadow)">
      <path d="M661 681 H870 L919 723 L870 766 H661 Z" fill="url(#band-blue)"/>
      <rect x="625" y="687" width="72" height="72" rx="6" transform="rotate(45 661 723)" fill="url(#gem-blue)"/>
      <text class="step-number" x="661" y="742" text-anchor="middle">5</text>
      <text class="step-title" x="715" y="722">EXERCISE</text>
      <text class="step-action" x="738" y="749">Move It</text>
    </g>
  </svg>

  <div class="emblem-fist" role="img" aria-label="White line illustration of a raised clenched fist, symbol of the Inner Uprising"></div>
</main>
</body>
</html>
```